ticket wallet design

We are a travel agent, need a design for our PVC resealable ticket wallet - size 27cm X 17.5cm. would like the design be colorful , delightful and looking forward to their trip. need our logo on it as well, logo size and color can be vary.
prefer simple design, not too complicated

Designs look the same

• world landmarks or photos...
• OR the whole design stays simple colorful and delightful.

```html
<!DOCTYPE html>
<html lang="en">
<head>
<meta charset="utf-8">
<title>Ticket Wallet – Front and Back</title>
<link rel="stylesheet" href="https://fonts.googleapis.com/css2?family=Cinzel:wght@500&family=Noto+Serif+SC:wght@500&display=swap">
<style>
  :root {
    --paper: #ffffff;
    --bg-light: #d3d6e4;
    --bg-deep: #8f9acb;
    --teal: #3aa996;
    --blue: #5b8ec6;
    --violet: #7f87c9;
    --frame: #ecedf0;
    --ink: #2c3a78;
    --ink-soft: #3a3f52;
    --rule: #6b6f7e;
  }
  * { margin: 0; padding: 0; box-sizing: border-box; }
  html, body {
    width: 815px; height: 1200px; overflow: hidden;
    background: var(--paper);
  }
  .canvas { position: relative; width: 815px; height: 1200px; }
  .wallet-face { position: absolute; display: block; }
  .wallet-face--front { left: 14px; top: 73px; width: 738px; height: 477px; }
  .wallet-face--back { left: 22px; top: 611px; width: 743px; height: 478px; outline: 1px solid #555; }
  .brand-name { font-family: "Cinzel", "Times New Roman", serif; font-weight: 500; fill: var(--ink-soft); }
  .brand-name-cn { font-family: "Noto Serif SC", "Songti SC", serif; font-weight: 500; fill: var(--ink-soft); }
  .brand-rule { stroke: var(--rule); stroke-width: 1; }
  .brand-dot { fill: var(--blue); }
  .tile { mix-blend-mode: multiply; }
  .photo-frame { stroke: var(--frame); stroke-width: 16; stroke-linejoin: miter; }
</style>
</head>
<body>
<main class="canvas">

  <!-- Front face -->
  <svg class="wallet-face wallet-face--front" viewBox="0 0 930 600" preserveAspectRatio="none">
    <defs>
      <linearGradient id="faceBg" x1="0" y1="0" x2="1" y2="0.4">
        <stop offset="0" stop-color="var(--bg-light)"/>
        <stop offset="1" stop-color="var(--bg-deep)"/>
      </linearGradient>
      <linearGradient id="sunset" x1="0" y1="0" x2="0" y2="1">
        <stop offset="0" stop-color="#c33a1e"/><stop offset="0.6" stop-color="#e07a2a"/><stop offset="1" stop-color="#2a1c14"/>
      </linearGradient>
      <linearGradient id="skyDay" x1="0" y1="0" x2="0" y2="1">
        <stop offset="0" stop-color="#4a86c9"/><stop offset="1" stop-color="#cfe0ef"/>
      </linearGradient>
      <linearGradient id="hills" x1="0" y1="0" x2="0" y2="1">
        <stop offset="0" stop-color="#7fb0dd"/><stop offset="0.45" stop-color="#b9d2e6"/><stop offset="0.55" stop-color="#4f8a3c"/><stop offset="1" stop-color="#2f6b2a"/>
      </linearGradient>
      <linearGradient id="forest" x1="0" y1="0" x2="0" y2="1">
        <stop offset="0" stop-color="#5b8fc4"/><stop offset="0.5" stop-color="#c25a2a"/><stop offset="1" stop-color="#3f6a3a"/>
      </linearGradient>
      <clipPath id="faceClipA"><rect width="930" height="600"/></clipPath>
    </defs>
    <g clip-path="url(#faceClipA)">
      <rect width="930" height="600" fill="url(#faceBg)"/>
      <g class="tiles">
        <rect class="tile" x="170" y="-60" width="160" height="160" fill="var(--teal)" opacity=".75" transform="rotate(45 250 20)"/>
        <rect class="tile" x="330" y="20" width="150" height="150" fill="var(--blue)" opacity=".45" transform="rotate(45 405 95)"/>
        <rect class="tile" x="470" y="-40" width="170" height="170" fill="var(--blue)" opacity=".5" transform="rotate(45 555 45)"/>
        <rect class="tile" x="600" y="60" width="170" height="170" fill="var(--violet)" opacity=".55" transform="rotate(45 685 145)"/>
        <rect class="tile" x="760" y="-20" width="170" height="170" fill="var(--teal)" opacity=".55" transform="rotate(45 845 65)"/>
        <rect class="tile" x="120" y="170" width="130" height="130" fill="var(--violet)" opacity=".35" transform="rotate(45 185 235)"/>
        <rect class="tile" x="290" y="200" width="110" height="110" fill="var(--teal)" opacity=".45" transform="rotate(45 345 255)"/>
        <rect class="tile" x="-40" y="420" width="120" height="120" fill="var(--teal)" opacity=".6" transform="rotate(45 20 480)"/>
        <rect class="tile" x="840" y="180" width="110" height="110" fill="var(--blue)" opacity=".5" transform="rotate(45 895 235)"/>
      </g>

      <g class="brand">
        <circle class="brand-dot" cx="70" cy="118" r="16"/>
        <text class="brand-name" x="94" y="126" font-size="21">Horizon Bridge Travel SA</text>
        <line class="brand-rule" x1="90" y1="146" x2="155" y2="146"/>
        <text class="brand-name-cn" x="222" y="153" font-size="19" text-anchor="middle">远航旅行社</text>
        <line class="brand-rule" x1="290" y1="146" x2="350" y2="146"/>
      </g>

      <g class="photo-tiles">
        <polygon class="photo-frame" role="img" aria-label="Photo: harbour opera house at sunset" points="207,248 397,438 207,628 12,438" fill="url(#sunset)"/>
        <polygon class="photo-frame" role="img" aria-label="Photo: iron lattice tower against blue sky" points="457,208 577,318 457,428 337,318" fill="url(#skyDay)"/>
        <polygon class="photo-frame" role="img" aria-label="Photo: leaning bell tower" points="397,463 492,558 397,653 302,558" fill="url(#skyDay)"/>
        <polygon class="photo-frame" role="img" aria-label="Photo: ancient wall winding over green mountains" points="647,268 837,448 647,628 472,443" fill="url(#hills)"/>
        <polygon class="photo-frame" role="img" aria-label="Photo: red pagoda among forested hills" points="832,208 942,318 832,428 742,318" fill="url(#forest)"/>
        <polygon class="photo-frame" role="img" aria-label="Photo: harbour statue against sky" points="862,478 972,588 862,698 752,588" fill="url(#skyDay)"/>
      </g>
    </g>
  </svg>

  <!-- Back face -->
  <svg class="wallet-face wallet-face--back" viewBox="0 0 930 600" preserveAspectRatio="none">
    <defs>
      <linearGradient id="faceBgB" x1="0" y1="0" x2="1" y2="0.4">
        <stop offset="0" stop-color="var(--bg-light)"/>
        <stop offset="1" stop-color="var(--bg-deep)"/>
      </linearGradient>
      <linearGradient id="falls" x1="0" y1="0" x2="0" y2="1">
        <stop offset="0" stop-color="#6fa6d6"/><stop offset="0.45" stop-color="#e4eef5"/><stop offset="1" stop-color="#2f7f95"/>
      </linearGradient>
      <linearGradient id="dusk" x1="0" y1="0" x2="0" y2="1">
        <stop offset="0" stop-color="#4b5fa8"/><stop offset="0.7" stop-color="#b48ab8"/><stop offset="1" stop-color="#2a2a40"/>
      </linearGradient>
      <linearGradient id="bridgeNight" x1="0" y1="0" x2="0" y2="1">
        <stop offset="0" stop-color="#5a6fb4"/><stop offset="0.55" stop-color="#a2577a"/><stop offset="0.75" stop-color="#d9742c"/><stop offset="1" stop-color="#1d2c52"/>
      </linearGradient>
      <linearGradient id="stone" x1="0" y1="0" x2="0" y2="1">
        <stop offset="0" stop-color="#7fa3d2"/><stop offset="0.3" stop-color="#c9a56c"/><stop offset="1" stop-color="#8b6a3e"/>
      </linearGradient>
      <linearGradient id="marble" x1="0" y1="0" x2="0" y2="1">
        <stop offset="0" stop-color="#c9c2b4"/><stop offset="1" stop-color="#8e8677"/>
      </linearGradient>
      <clipPath id="faceClipB"><rect width="930" height="600"/></clipPath>
    </defs>
    <g clip-path="url(#faceClipB)">
      <rect width="930" height="600" fill="url(#faceBgB)"/>
      <g class="tiles">
        <rect class="tile" x="170" y="-60" width="160" height="160" fill="var(--teal)" opacity=".75" transform="rotate(45 250 20)"/>
        <rect class="tile" x="330" y="20" width="150" height="150" fill="var(--blue)" opacity=".45" transform="rotate(45 405 95)"/>
        <rect class="tile" x="470" y="-40" width="170" height="170" fill="var(--blue)" opacity=".5" transform="rotate(45 555 45)"/>
        <rect class="tile" x="600" y="40" width="170" height="170" fill="var(--violet)" opacity=".55" transform="rotate(45 685 125)"/>
        <rect class="tile" x="760" y="-20" width="170" height="170" fill="var(--teal)" opacity=".55" transform="rotate(45 845 65)"/>
        <rect class="tile" x="200" y="230" width="110" height="110" fill="var(--teal)" opacity=".45" transform="rotate(45 255 285)"/>
        <rect class="tile" x="-40" y="300" width="120" height="120" fill="var(--teal)" opacity=".6" transform="rotate(45 20 360)"/>
        <rect class="tile" x="840" y="150" width="110" height="110" fill="var(--blue)" opacity=".5" transform="rotate(45 895 205)"/>
      </g>

      <g class="brand">
        <circle class="brand-dot" cx="62" cy="155" r="24"/>
        <text class="brand-name" x="94" y="178" font-size="34">Horizon Bridge Travel SA</text>
        <line class="brand-rule" x1="112" y1="208" x2="240" y2="208"/>
        <text class="brand-name-cn" x="327" y="220" font-size="30" text-anchor="middle">远航旅行社</text>
        <line class="brand-rule" x1="414" y1="208" x2="540" y2="208"/>
      </g>

      <g class="photo-tiles">
        <polygon class="photo-frame" role="img" aria-label="Photo: waterfall with tour boat" points="112,292 312,492 112,692 -88,492" fill="url(#falls)"/>
        <polygon class="photo-frame" role="img" aria-label="Photo: skyscraper skyline at dusk" points="357,237 477,357 357,477 237,357" fill="url(#dusk)"/>
        <polygon class="photo-frame" role="img" aria-label="Photo: windmills at twilight" points="452,442 577,567 452,692 327,567" fill="url(#dusk)"/>
        <polygon class="photo-frame" role="img" aria-label="Photo: suspension bridge lit at night" points="642,217 832,407 642,597 452,407" fill="url(#bridgeNight)"/>
        <polygon class="photo-frame" role="img" aria-label="Photo: ancient temple with carved columns" points="842,172 962,292 842,412 722,292" fill="url(#stone)"/>
        <polygon class="photo-frame" role="img" aria-label="Photo: baroque fountain sculpture" points="832,462 952,582 832,702 712,582" fill="url(#marble)"/>
      </g>
    </g>
  </svg>

</main>
</body>
</html>
```